Law Firm Logo and Stationary

I need a logo for my law firm.  The logo should only contain the firm name "Harlow & Harlow, P.C." but we are open to slight additions like underlining or a box.  We are looking for a modern style but not edgy because our target market is businesses and corporations.

I would like a logo that invokes the traditional values of a law firm (trust, integrity, knowledge) but I want an updated look.

To be clear, the logo should only contain the firm name, I am just looking for a font treatment.

The logo color is up to you.  The only initial opinion I have is that bright colors may not fit with the professional look of a law firm. 

I also want to incorporate the new logo into letterhead and business card designs.  The letterhead should include all of the information that is in my current letterhead, which is attached.  The letterhead should be black or grey on white.  The colored logo will go on the website and promotional materials.

For the business card, I would like to have the logo on the top left, the employee name (Colin J. Harlow) on the middle left and the firm information (address, tel, fax, website, email) on right side.  I am open to suggestions if you have better ideas.
Updates

Here are some comments on the initial 8 designs:

a) I am just interested in a font treatment of our firm name, "Harlow & Harlow, P.C."  I do not want any graphics like a gavel or shield. 

b) The full name of the firm must be in the logo.  So I cannot use designs that only have "H & H"

c) EXAMPLES: Here are two websites with examples of law firm logos that just have the firm name.  These are just samples to give you a general idea of what I am looking for.  Check out:  www.qx-legalco.com and www.tarrowmeade-law.com 

In short, I am looking for a simple, clean design that will look modern enough for our website but is also conservative enough to be on letterhead that gets sent to judges and other lawyers.

Also, the sample letterhead is now loaded in the brief so you can see the information I need included in the new letterhead.

Thanks.

Target Market(s)

businesses and corporations.

Industry/Entity Type

Law Firm

Logo Text

Harlow & Harlow, P.C.

Requirements
Must have
• Firm name, "Harlow & Harlow, P.C."

```html
<!DOCTYPE html>
<html lang="en">
<head>
<meta charset="utf-8">
<title>Harlow &amp; Harlow, P.C. — Stationery</title>
<link href="https://fonts.googleapis.com/css2?family=Cormorant+SC:wght@500&family=Cormorant+Garamond:wght@500&family=Lato:wght@400&display=swap" rel="stylesheet">
<style>
  :root {
    --paper: #ffffff;
    --ink: #2a2a2a;
    --rule: #a8a8a8;
    --shadow: rgba(0, 0, 0, 0.35);
  }
  html, body {
    margin: 0;
    width: 927px;
    height: 1200px;
    overflow: hidden;
    background: var(--paper);
  }
  .sheet {
    position: relative;
    width: 927px;
    height: 1200px;
    color: var(--ink);
    font-family: "Cormorant Garamond", Georgia, serif;
  }

  /* Wordmark: firm name in one colour, one weight */
  .wordmark {
    position: absolute;
    font-family: "Cormorant SC", Georgia, serif;
    font-weight: 500;
    color: var(--ink);
    white-space: nowrap;
    line-height: 1;
  }
  .tagline {
    position: absolute;
    font-family: "Lato", Arial, sans-serif;
    color: var(--ink);
    white-space: nowrap;
    line-height: 1;
  }

  /* Letterhead */
  .letterhead .wordmark { left: 54px; top: 58px; font-size: 28px; }
  .letterhead .tagline  { left: 97px; top: 105px; font-size: 12.5px; letter-spacing: 5.6px; }

  .letterhead-info {
    position: absolute;
    left: 560px;
    top: 50px;
    font-size: 13px;
    line-height: 17px;
    color: var(--ink);
  }
  .letterhead-info .sc { font-family: "Cormorant SC", Georgia, serif; }
  .sep { color: var(--rule); padding: 0 5px; }
  .partners {
    margin-top: 6px;
    display: flex;
    gap: 12px;
    font-family: "Cormorant SC", Georgia, serif;
    font-size: 13px;
    white-space: nowrap;
  }
  .partner { position: relative; }
  .partner .years {
    position: absolute;
    right: 0;
    top: 15px;
    font-family: "Cormorant Garamond", Georgia, serif;
    font-size: 9px;
  }
  .admission { margin-top: 12px; font-size: 9.5px; line-height: 12px; }
  .admission .sc { font-size: 10.5px; }

  /* Business card */
  .business-card {
    position: absolute;
    left: 479px;
    top: 589px;
    width: 354px;
    height: 162px;
    background: var(--paper);
    box-shadow: 2px 3px 6px var(--shadow);
  }
  .business-card .wordmark { left: 10px; top: 12px; font-size: 16px; }
  .business-card .tagline  { left: 30px; top: 36px; font-size: 7.5px; letter-spacing: 2.4px; }
  .card-name {
    position: absolute;
    left: 30px;
    top: 93px;
    font-family: "Lato", Arial, sans-serif;
    font-size: 11.5px;
    color: var(--ink);
  }
  .card-divider {
    position: absolute;
    left: 171px;
    top: 72px;
    width: 1px;
    height: 78px;
    background: var(--rule);
  }
  .card-info {
    position: absolute;
    left: 180px;
    top: 74px;
    font-size: 9.5px;
    line-height: 12px;
    white-space: nowrap;
  }
  .card-info .sc { font-family: "Cormorant SC", Georgia, serif; }
  .card-info .web { margin-top: 16px; }

  /* Envelope */
  .envelope {
    position: absolute;
    left: 50px;
    top: 808px;
    width: 853px;
    height: 330px;
    background: var(--paper);
    box-shadow: 2px 3px 7px var(--shadow);
  }
  .envelope .wordmark { left: 22px; top: 22px; font-size: 16.5px; }
  .envelope .tagline  { left: 48px; top: 46px; font-size: 7.5px; letter-spacing: 2.4px; }
  .envelope-divider {
    position: absolute;
    left: 205px;
    top: 18px;
    width: 1px;
    height: 42px;
    background: var(--rule);
  }
  .return-address {
    position: absolute;
    left: 214px;
    top: 22px;
    font-family: "Cormorant SC", Georgia, serif;
    font-size: 11px;
    line-height: 14px;
    white-space: nowrap;
  }
</style>
</head>
<body>
<main class="sheet">

  <section class="letterhead">
    <div class="wordmark">Harlow &amp; Harlow, P.C.</div>
    <div class="tagline">ATTORNEYS AT LAW</div>

    <div class="letterhead-info">
      <div><span class="sc">2715 Linden Avenue</span><span class="sep">|</span><span class="sc">Oakridge, Maryland 20990</span></div>
      <div>T 301.555.0142<span class="sep">|</span>F 301.555.0187</div>
      <div>martin.harlow@harlowlegalpc.com<span class="sep">|</span>www.harlowlegalpc.com</div>
      <div class="partners">
        <span class="partner">Martin E. Harlow †#</span>
        <span class="partner">Colin J. Harlow †*</span>
        <span class="partner">Walter Harlow<span class="years">(1916–1994)</span></span>
      </div>
      <div class="admission">
        <div class="sc">Admitted to Practice</div>
        <div>†District of Columbia &nbsp;#Maryland &nbsp;*New York</div>
      </div>
    </div>
  </section>

  <section class="business-card">
    <div class="wordmark">Harlow &amp; Harlow, P.C.</div>
    <div class="tagline">ATTORNEYS AT LAW</div>
    <div class="card-name">Martin E. Harlow</div>
    <div class="card-divider"></div>
    <div class="card-info">
      <div class="sc">2715 Linden Avenue</div>
      <div class="sc">Oakridge, Maryland 20990</div>
      <div>T 301.555.0142<span class="sep">|</span>F 301.555.0187</div>
      <div class="web">martin.harlow@harlowlegalpc.com</div>
      <div>www.harlowlegalpc.com</div>
    </div>
  </section>

  <section class="envelope">
    <div class="wordmark">Harlow &amp; Harlow, P.C.</div>
    <div class="tagline">ATTORNEYS AT LAW</div>
    <div class="envelope-divider"></div>
    <div class="return-address">
      <div>2715 Linden Avenue</div>
      <div>Oakridge, Maryland 20990</div>
    </div>
  </section>

</main>
</body>
</html>
```